Print design needed to improve the layout and look of some existing documents

We need someone to take a couple of existing documents that we have and make them look much better using our existing logo and corporate colors etc. We require these to be delivered in a format that will allow our staff to edit the content as necessary via Microsoft word for conversion once finalized into a PDF. Ideally, we will also be able to use this as a newsletter template or for other documents that might be required in our business. www.calderfinch.com.au
Updates

Project Deadline Extended Reason: So far, I have only seen one design that I believe is quite good quality. Added Sunday, July 3, 2016

Target Market(s)

Business owners, executives, retirees

Industry/Entity Type

Financial Service

Font styles to use
Serif

Requirements
Must have
• Design that uses our existing branding and colors. It also needs to be ina form that we can edit the content / update easily. Ideally the format / layout could also be used for other documents such as short newsletters etc.
Nice to have
• Fresh, simple and crisp. Very professional looking.
Should not have
• strange fonts, weird layouts.

```html
<!DOCTYPE html>
<html lang="en">
<head>
<meta charset="utf-8">
<title>Your Financial Advisers – Calder Finch</title>
<link href="https://fonts.googleapis.com/css2?family=Nunito:ital,wght@0,400;0,700;0,800;1,400&display=swap" rel="stylesheet">
<style>
  :root {
    --brand-blue: #1e9be0;
    --brand-green: #62b246;
    --brand-navy: #1d3f6e;
    --ink: #2b2b2b;
    --paper: #ffffff;
    --photo-a: #8d9a86;
    --photo-b: #4b5a66;
  }
  * { margin: 0; padding: 0; box-sizing: border-box; }
  html, body { width: 832px; height: 1200px; overflow: hidden; background: var(--paper); }
  body { position: relative; font-family: "Nunito", sans-serif; color: var(--ink); }

  .edge-band {
    position: absolute; top: 0; right: 0; width: 29px; height: 1200px;
    background: linear-gradient(to bottom, var(--brand-blue), var(--brand-green));
  }

  .section-tab { position: absolute; height: 51px; }
  .section-tab svg { position: absolute; inset: 0; }
  .section-tab h2 {
    position: relative; font-weight: 800; font-size: 18px; color: #fff;
    line-height: 51px; padding-left: 8px; letter-spacing: -0.2px;
  }
  .tab-advisers { left: 15px; top: 62px; width: 244px; }
  .tab-process { left: 413px; top: 639px; width: 300px; }

  .portrait { position: absolute; width: 175px; height: 184px; }

  .copy {
    position: absolute; font-style: italic; font-size: 13.2px; line-height: 20px;
    text-align: justify;
  }
  .copy p + p { margin-top: 20px; }
  .drop { font-size: 20px; }

  .page-number {
    position: absolute; left: 692px; top: 1157px; font-size: 16px; color: var(--ink);
  }
</style>
</head>
<body>

<div class="edge-band"></div>

<div class="section-tab tab-advisers">
  <svg width="244" height="51" viewBox="0 0 244 51">
    <path d="M0 0 H236 Q244 0 244 8 V51 H0 Z" fill="var(--brand-blue)"/>
    <path d="M190 0 H236 Q244 0 244 8 V51 Z" fill="var(--brand-green)"/>
    <path d="M192 0 L244 51" stroke="var(--brand-navy)" stroke-width="3"/>
  </svg>
  <h2>Your Financial Advisers</h2>
</div>

<!-- Adviser one -->
<svg class="portrait" style="left:18px;top:160px" viewBox="0 0 175 184" role="img" aria-label="Portrait photograph of Grant Holloway">
  <defs><linearGradient id="ph1" x1="0" y1="0" x2="0" y2="1"><stop offset="0" stop-color="var(--photo-a)"/><stop offset="1" stop-color="var(--photo-b)"/></linearGradient></defs>
  <polygon points="0,0 152,0 104,160 0,170" fill="url(#ph1)"/>
  <polygon points="164,0 174,0 124,150 114,152" fill="var(--brand-green)"/>
  <polygon points="12,184 10,172 124,150 120,162" fill="var(--brand-blue)"/>
  <rect x="60" y="158" width="102" height="20" fill="#fff"/>
  <text x="111" y="173" text-anchor="middle" font-family="Nunito, sans-serif" font-style="italic" font-size="14" fill="#1a1a1a">Grant Holloway</text>
</svg>
<div class="copy" style="left:199px;top:170px;width:136px">
  <p><span class="drop">G</span>rant Holloway is the Managing Director of Calder Finch Pty Ltd. He has been providing financial planning and investment advice to clients since 1993. Prior to forming</p>
</div>
<div class="copy" style="left:18px;top:374px;width:317px">
  <p>Calder Finch, he has been director and part owner of Harbourline Investment &amp; Retirement Services Pty Ltd since 1998.</p>
  <p>He holds a Bachelor of Business in Accounting &amp; Finance, a graduate diploma in Financial Planning and is a SFN Self-Managed Super Specialist™. He is a member of the Planning Professionals Guild (PPG), a Fellow of the Finance Practitioners Institute and is a member of the Adviser Practice Council (APC).</p>
</div>

<!-- Adviser two -->
<svg class="portrait" style="left:420px;top:160px" viewBox="0 0 175 184" role="img" aria-label="Portrait photograph of Mark Ellery">
  <defs><linearGradient id="ph2" x1="0" y1="0" x2="0" y2="1"><stop offset="0" stop-color="#9aa9a0"/><stop offset="1" stop-color="#3c4650"/></linearGradient></defs>
  <polygon points="0,0 152,0 104,160 0,170" fill="url(#ph2)"/>
  <polygon points="164,0 174,0 124,150 114,152" fill="var(--brand-green)"/>
  <polygon points="12,184 10,172 124,150 120,162" fill="var(--brand-blue)"/>
  <rect x="60" y="158" width="102" height="20" fill="#fff"/>
  <text x="111" y="173" text-anchor="middle" font-family="Nunito, sans-serif" font-style="italic" font-size="14" fill="#1a1a1a">Mark Ellery</text>
</svg>
<div class="copy" style="left:601px;top:170px;width:136px">
  <p><span class="drop">M</span>ark Ellery has been providing financial planning and investment advice to clients since 1999.</p>
  <p>He has five years specific financial planning and invest-</p>
</div>
<div class="copy" style="left:420px;top:354px;width:317px">
  <p>ment advice experience and an additional 10 years in banking and general insurance.</p>
  <p>He holds an Advanced Diploma in Financial Planning, a Diploma in Finance/Mortgage Broking and is currently working towards completing a Bachelor of Commerce at Kestrel University.</p>
  <p>Grant Holloway, Peter Vasilakis and Mark Ellery will provide these services to you as Authorised Representatives of Calder Finch Pty Ltd. They act on behalf of Calder Finch Pty Ltd which is responsible for the services they provide.</p>
</div>

<!-- Adviser three -->
<svg class="portrait" style="left:18px;top:643px" viewBox="0 0 175 184" role="img" aria-label="Portrait photograph of Peter Vasilakis">
  <defs><linearGradient id="ph3" x1="0" y1="0" x2="0" y2="1"><stop offset="0" stop-color="#a2ad95"/><stop offset="1" stop-color="#3f4348"/></linearGradient></defs>
  <polygon points="0,0 152,0 104,160 0,170" fill="url(#ph3)"/>
  <polygon points="164,0 174,0 124,150 114,152" fill="var(--brand-green)"/>
  <polygon points="12,184 10,172 124,150 120,162" fill="var(--brand-blue)"/>
  <rect x="54" y="158" width="110" height="20" fill="#fff"/>
  <text x="109" y="173" text-anchor="middle" font-family="Nunito, sans-serif" font-style="italic" font-size="14" fill="#1a1a1a">Peter Vasilakis</text>
</svg>
<div class="copy" style="left:199px;top:653px;width:136px">
  <p><span class="drop">P</span>eter Vasilakis chairs the investment committee of Calder Finch Pty Ltd. He has many decades of experience in the financial services industry.</p>
</div>
<div class="copy" style="left:18px;top:856px;width:317px">
  <p>He was Director Private Banking at Eastgate Bank from 2009 to 2010 and was State Manager Broker Mortgage Services at Eastgate Bank from 2005 to 2006. He also held a variety of senior positions within the Westmere Bank of Australia where he served as an employee for over 30 years.</p>
  <p>He has extensive management and leadership skills and he holds a Diploma of Financial Planning from the Harbour Institute of Technology.</p>
</div>

<div class="section-tab tab-process">
  <svg width="300" height="51" viewBox="0 0 300 51">
    <path d="M0 0 H292 Q300 0 300 8 V51 H0 Z" fill="var(--brand-blue)"/>
    <path d="M246 0 H292 Q300 0 300 8 V51 Z" fill="var(--brand-green)"/>
    <path d="M248 0 L300 51" stroke="var(--brand-navy)" stroke-width="3"/>
  </svg>
  <h2>The financial advice process</h2>
</div>

<div class="copy" style="left:420px;top:713px;width:317px">
  <p>We recognise that the objectives and personal circumstances of each client are different. <br>We understand that what is right for one client may not be right for another.</p>
  <p>We will listen to you to understand your objectives and circumstances. We will also ask questions to make sure we address all relevant issues.</p>
  <p>When we first provide advice to you it will be explained thoroughly and documented in a Statement of Advice which you can take away and study.</p>
  <p>The Statement of Advice will explain the basis for the advice, the cost to you of implementing the advice and any fees associated with the advice.</p>
</div>

<div class="page-number">Page 3 of 6</div>

</body>
</html>
```